Corvallin Property Solutions need a business card design

Hello guys. We would need a business card design asap please.
We are a start up property investment business based in London UK specialised in buying, selling, managing and letting properties and helping distressed property owners.
The name of our Business is Corvallin, the logo symbolises the four fundamental elements of the world (earth, air, fire and water) and so it stands for strength, stability, longevity.
We would like the business card to communicate professionalism and reliability. Many many thanks indeed for your work.

Details:

1.) Marisol Dunkley
Property Investor
Mobile: +44(0)7700362517
Email: marisol.corvallin@quilbrook.example

2.) Tomas Brindle
Property Investor
Mobile: +44(0)7700845926
Email: tomas.corvallin@quilbrook.example

Industry/Entity Type

Investment

```html
<!DOCTYPE html>
<html lang="en">
<head>
<meta charset="utf-8">
<title>Corvallin Property Solutions — Business Card</title>
<link rel="stylesheet" href="https://fonts.googleapis.com/css2?family=Open+Sans:wght@400;600;700&display=swap">
<style>
  :root {
    --backdrop-light: #eceef0;
    --backdrop-dark: #d9dbde;
    --card-white: #ffffff;
    --ink-dark: #1c1c1c;
    --ink-grey: #8e8e8e;
    --band-red: #e8202e;
    --band-red-deep: #c4121f;
    --band-green: #1fae3c;
    --band-green-deep: #138a2b;
    --band-blue: #2f63c6;
    --band-blue-deep: #1f4ba3;
  }
  * { box-sizing: border-box; margin: 0; padding: 0; }
  html, body { width: 1200px; height: 800px; overflow: hidden; }
  body {
    background: radial-gradient(ellipse at 50% 40%, var(--backdrop-light), var(--backdrop-dark));
    font-family: "Open Sans", Arial, sans-serif;
    display: flex;
    align-items: center;
    justify-content: center;
    gap: 60px;
  }
  .business-card {
    position: relative;
    width: 525px;
    height: 300px;
    background: var(--card-white);
    box-shadow: 0 2px 3px rgba(0,0,0,0.08), 0 14px 30px rgba(0,0,0,0.10);
    overflow: hidden;
  }
  .colour-band {
    position: absolute;
    left: 0; right: 0; bottom: 0;
    height: 22px;
    display: flex;
  }
  .colour-band span { flex: 1; }
  .band-red   { background: linear-gradient(135deg, var(--band-red), var(--band-red-deep)); }
  .band-green { background: linear-gradient(135deg, var(--band-green), var(--band-green-deep)); }
  .band-blue  { background: linear-gradient(135deg, var(--band-blue), var(--band-blue-deep)); }

  .brand-lockup { display: flex; align-items: center; gap: 14px; }
  .brand-square { width: 34px; height: 34px; flex: none; }
  .brand-name { line-height: 1.05; letter-spacing: 0.5px; }

  .card-front .brand-lockup {
    position: absolute;
    top: 110px; left: 130px;
  }
  .card-front .brand-square { background: var(--ink-grey); }
  .card-front .brand-name {
    color: var(--ink-grey);
    font-weight: 600;
    font-size: 26px;
  }
  .card-front .brand-name small { display: block; font-size: 19px; font-weight: 600; }

  .card-back .brand-lockup {
    position: absolute;
    top: 70px; left: 58px;
  }
  .card-back .brand-square { width: 24px; height: 24px; background: var(--ink-dark); }
  .card-back .brand-name {
    color: var(--ink-dark);
    font-weight: 700;
    font-size: 17px;
  }
  .card-back .brand-name small { display: block; font-size: 10px; font-weight: 700; }

  .contact-details {
    position: absolute;
    top: 118px; left: 330px;
    color: var(--ink-dark);
    font-size: 11.5px;
    line-height: 1.35;
  }
  .contact-name { font-size: 19px; font-weight: 400; margin-bottom: 4px; }
</style>
</head>
<body>
  <section class="business-card card-front" aria-label="Card front">
    <div class="brand-lockup">
      <span class="brand-square"></span>
      <p class="brand-name">CORVALLIN<small>PROPERTY SOLUTIONS</small></p>
    </div>
    <div class="colour-band">
      <span class="band-red"></span><span class="band-green"></span><span class="band-blue"></span><span class="band-red"></span><span class="band-green"></span>
    </div>
  </section>

  <section class="business-card card-back" aria-label="Card back">
    <div class="brand-lockup">
      <span class="brand-square"></span>
      <p class="brand-name">CORVALLIN<small>PROPERTY SOLUTIONS</small></p>
    </div>
    <div class="contact-details">
      <p class="contact-name">Arlen Pryce</p>
      <p>Director</p>
      <p>Phone:(555) 014-2286</p>
      <p>18 Fenmore Lane</p>
      <p>Harrowmere, ZS</p>
      <p>(Zedshire) 00417</p>
    </div>
    <div class="colour-band">
      <span class="band-red"></span><span class="band-green"></span><span class="band-blue"></span><span class="band-red"></span><span class="band-green"></span>
    </div>
  </section>
</body>
</html>
```